Web Design Project

My website was fine - years ago. But it's way, way overdue for an overhaul. When I started my business almost 20 years ago, I wanted to be edgy. And my website was just that. Color, style, voice. Edgy. Today, my clients are corporations. I'm older, more experienced - but still a little edgy. It's controlled edge. What I want now is sophisticated. Savvy. Corporate but cool. Grown up.

My clients are primarily - but not exclusively - in healthcare. But I don't want a healthcare site. I provide the following services:
1. Writing - white papers, brochures, web pages, speechwriting, etc.
2. Marketing strategy
3. Public relations services
4. Thought leader development
5. Training
I couldn't upload all the icons but I can send them. They correspond with the pages as follows and should be used in the design:

1. Writing- nib.png
2. Marketing strategy-compass.png
3. Public relations services-microphone.png
4. Thought leader development-lightbulb.png
5. Training: cogs-training.png or key.png

I will have a blog, and a portfolio of some kind.

I don't want something that looks like a template.
Updates

Project Deadline Extended
Reason: Just made this a committed payment. I apologize for not doing so from the start. Nobody should work for free.

Project Deadline Extended
Reason: Several folks have asked to resubmit, and it has taken me a while to provide feedback.

Dear Designers,

I am so sorry to have been so slow to select. I've had professional and personal issues to deal with. I am actively trying to select a design, however, and will do so in the next two days. Thanks so much for your patience and hard work.

Marla

Thanks so much to everyone who has submitted a design. I had great luck crowdsourcing my logo, but I'm starting to realize that website design is a totally different animal. All of your designs are great, but they all look exactly like templates. And maybe that's the way it's supposed to be, the way it should be. I don't want to use stock photography. It needs to be more personalized than that. I'm open to illustration or even using my own photo on the site, but stock photography won't work for me. If anyone wants to submit something else - and I understand if you don't - please feel free. 

Target Market(s)

C-suite executives; corporations, larger businesses who need marketing writing

Industry/Entity Type

Healthcare

Requirements
Must have
• Logo (somewhere)
Icons
Nice to have
• Level-specific page design (e.g, Home = Level 1, Tabs = Level 2, etc). I'd like it to have a certain order.

```html
<!DOCTYPE html>
<html lang="en">
<head>
<meta charset="utf-8">
<title>The Vantage Communication</title>
<link href="https://fonts.googleapis.com/css2?family=Roboto:ital,wght@0,400;0,500;0,700;1,400;1,500&family=Roboto+Condensed:wght@400;700&family=Fjalla+One&family=Open+Sans:wght@400;600&display=swap" rel="stylesheet">
<style>
:root{
  --orange:#f7931e;
  --orange-btn:#f9a03a;
  --purple:#5c2d86;
  --ink:#333333;
  --muted:#8a8a8a;
  --line:#dddddd;
  --page:#e7e7e7;
  --panel:#f4f4f4;
  --white:#ffffff;
  --band:#3c3c3c;
  --footer:#404040;
}
*{box-sizing:border-box;margin:0;padding:0}
html,body{width:1200px;height:2371px;overflow:hidden}
body{background:var(--page);font-family:"Roboto",Arial,sans-serif;color:var(--ink);position:relative}
.abs{position:absolute}
.btn{position:absolute;display:flex;align-items:center;justify-content:center;background:var(--orange-btn);color:var(--white);font-size:11px;height:31px;width:98px;border-radius:2px;box-shadow:0 1px 2px rgba(0,0,0,.2)}
.btn.purple{background:var(--purple)}
.lorem{font-size:12.5px;line-height:16px;color:var(--muted);text-align:justify}
.head{font-family:"Roboto Condensed",Arial,sans-serif;font-weight:400;font-size:19px;color:var(--ink);text-transform:uppercase;position:absolute}

/* header */
.topline{left:0;top:0;width:1200px;height:5px;background:var(--orange)}
.header{left:0;top:5px;width:1200px;height:129px;background:var(--white);border-bottom:3px solid var(--purple)}
.brand{left:90px;top:22px;display:flex;align-items:center;gap:10px}
.brand-mark{width:34px;height:34px;background:var(--purple);border-radius:50%}
.brand-name{font-family:"Roboto Condensed",Arial,sans-serif;font-weight:700;font-size:30px;color:var(--purple)}
.tollfree{right:79px;top:40px;font-size:14px;color:var(--purple)}
.nav{right:75px;top:84px;display:flex;gap:30px;font-size:15px;color:#222}
.nav span{padding:4px 8px}
.nav .active{background:var(--purple);color:var(--white);border-radius:3px}

/* hero */
.hero-band{left:0;top:137px;width:1200px;height:453px;background:var(--band)}
.hero-photo{left:75px;top:137px;width:1050px;height:453px;background:linear-gradient(90deg,#f3f3f3 0%,#ececec 45%,#d9c6b6 70%,#c9a58a 85%,#e8e2dc 100%)}
.hero-title{left:116px;top:240px;font-family:"Fjalla One",Arial,sans-serif;font-size:70px;line-height:88px;color:#3b3b3b}
.hero-title .hl{color:#f26b21}
.arrow{top:340px}

/* intro */
.intro{left:75px;top:590px;width:1050px;height:172px;background:var(--white);text-align:center}
.intro h1{position:absolute;top:26px;width:100%;font-family:"Open Sans",Arial,sans-serif;font-weight:400;font-size:39px;color:var(--orange)}
.intro p{position:absolute;top:74px;width:100%;font-family:"Open Sans",Arial,sans-serif;font-size:19px;color:var(--orange)}

/* three columns */
.cols{left:75px;top:762px;width:1050px;height:231px;background:var(--panel);border-bottom:1px solid var(--line)}
.col{position:absolute;top:0;width:313px;height:100%}
.col .head{top:22px;left:0}
.col .lorem{position:absolute;top:56px;left:0;width:313px}
.col .btn{top:155px;left:0}
.vline{position:absolute;top:40px;width:1px;height:150px;background:var(--line)}

/* services */
.services{left:75px;top:993px;width:1050px;height:359px;background:var(--panel);border-bottom:1px solid var(--line)}
.card{position:absolute;top:41px;width:196px;height:277px;background:var(--white)}
.card h3{position:absolute;top:8px;width:100%;text-align:center;font-family:"Roboto Condensed",Arial,sans-serif;font-weight:400;font-size:17px;line-height:20px;color:var(--ink)}
.card .badge{position:absolute;left:64px;top:53px;width:68px;height:68px;border-radius:50%;background:var(--purple);border:3px solid var(--orange)}
.card .lorem{position:absolute;left:14px;top:137px;width:168px;font-size:10.5px;line-height:13.5px;height:94px;overflow:hidden}
.card .more{position:absolute;left:0;bottom:0;width:100%;height:33px;background:var(--orange-btn);color:var(--white);font-size:15px;display:flex;align-items:center;justify-content:center;border-radius:0 0 4px 4px}
.card .more.on{background:var(--purple)}

/* welcome + news */
.mid{left:75px;top:1352px;width:1050px;height:557px;background:var(--panel);border-bottom:1px solid var(--line)}
.mid .divider{position:absolute;left:439px;top:15px;width:1px;height:520px;background:var(--line)}
.news-item{position:absolute;left:469px;width:576px;height:140px}
.news-img{position:absolute;left:0;top:0;width:177px;height:117px;border:3px solid #cfcfcf}
.news-date{position:absolute;left:202px;top:0;font-size:13px;color:var(--purple);text-decoration:underline}
.news-item .lorem{position:absolute;left:202px;top:28px;width:366px;font-size:13px;line-height:17px}
.quote{font-style:italic}

/* partners */
.folks{left:75px;top:1909px;width:1050px;height:154px;background:var(--panel)}
.partners{position:absolute;left:0;top:68px;width:1050px;height:86px;background:var(--white);display:flex;align-items:center;justify-content:space-around}
.partner{display:flex;align-items:center;gap:6px;font-size:17px;font-weight:500;color:#3f3f3f}
.partner i{display:block;width:14px;height:14px;background:#9aa6b2}

/* footer */
.footer{left:75px;top:2063px;width:1050px;height:274px;background:var(--footer);color:var(--white)}
.footer h4{position:absolute;top:24px;font-family:"Roboto Condensed",Arial,sans-serif;font-weight:400;font-size:15px}
.footer p,.footer li{font-size:11.5px;line-height:17px}
.footer ul{list-style:disc;padding-left:16px}
.footer .hot{color:var(--orange);text-decoration:underline}
.map{position:absolute;left:760px;top:60px;width:290px;height:197px;background:linear-gradient(135deg,#e9e3d3,#f3d87a 50%,#e6dfcf)}
.copy{left:75px;top:2337px;width:1050px;height:34px;background:var(--white);font-size:10px;font-weight:500;padding:10px 20px;color:#222}

/* social rail */
.social{left:0;top:668px;width:64px;height:205px;background:var(--white);border-radius:0 6px 6px 0;box-shadow:0 0 4px rgba(0,0,0,.2);display:flex;flex-direction:column;align-items:center;justify-content:center;gap:6px}
.social span{display:block;width:34px;height:34px;background:#8e8e8e;border-radius:3px}
</style>
</head>
<body>

<div class="abs topline"></div>
<header class="abs header">
  <div class="abs brand"><span class="brand-mark"></span><span class="brand-name">THE VANTAGE</span></div>
  <div class="abs tollfree">TOLL FREE: +18-(555)-010-274</div>
  <nav class="abs nav"><span>HOME</span><span class="active">ABOUT US</span><span>SERVICES</span><span>PORTFOLIO</span><span>OUR BLOG</span><span>CONTACT US</span></nav>
</header>

<section>
  <div class="abs hero-band"></div>
  <div class="abs hero-photo" role="img" aria-label="Portrait photo of a smiling consultant on a light backdrop"></div>
  <div class="abs hero-title"><div class="hl">HIGHLY</div><div>COMPREHENSIVE</div><div>HELP</div></div>
  <svg class="abs arrow" style="left:82px" width="24" height="50" viewBox="0 0 24 50"><path d="M20 4 4 25l16 21" fill="none" stroke="#777" stroke-width="4"/></svg>
  <svg class="abs arrow" style="left:1097px" width="24" height="50" viewBox="0 0 24 50"><path d="M4 4l16 21L4 46" fill="none" stroke="#777" stroke-width="4"/></svg>
</section>

<aside class="abs social" aria-label="Social links"><span></span><span></span><span></span><span></span></aside>

<section class="abs intro">
  <h1>Hello And Welcome to our site!</h1>
  <p>Our Writers ' Fills Your Paper With Breathing of Your Heart '</p>
  <div class="btn" style="left:476px;top:122px;height:29px">Read More ▾</div>
</section>

<section class="abs cols">
  <div class="col" style="left:7px"><h2 class="head">What we do!</h2><p class="lorem">Lorem Ipsum is simply dummy text of the printing and typesetting industry. Lorem Ipsum has been the industry's standard dummy text ever since the 1500s, when an unknown printer took a galley of type and scrambled it to make a type specimen book.</p><div class="btn">Read More &gt;&gt;</div></div>
  <div class="vline" style="left:344px"></div>
  <div class="col" style="left:372px"><h2 class="head">What's up</h2><p class="lorem">Lorem Ipsum is simply dummy text of the printing and typesetting industry. Lorem Ipsum has been the industry's standard dummy text ever since the 1500s, when an unknown printer took a galley of type and scrambled it to make a type specimen book.</p><div class="btn purple">Read More &gt;&gt;</div></div>
  <div class="vline" style="left:706px"></div>
  <div class="col" style="left:735px"><h2 class="head">Did you know?</h2><p class="lorem">Lorem Ipsum is simply dummy text of the printing and typesetting industry. Lorem Ipsum has been the industry's standard dummy text ever since the 1500s, when an unknown printer took a galley of type and scrambled it to make a type specimen book.</p><div class="btn">Read More &gt;&gt;</div></div>
</section>

<section class="abs services">
  <article class="card" style="left:0"><h3 style="top:18px">WRITING</h3><div class="badge" role="img" aria-label="Pen nib icon"></div><p class="lorem">Lorem Ipsum is simply dummy text of the printing and typesetting industry. Lorem Ipsum has been the industry's standard dummy text ever since the 1500s, when an unknown printer took a galley.</p><div class="more">READ MORE</div></article>
  <article class="card" style="left:213px"><h3>MARKETING<br>STRATEGY</h3><div class="badge" role="img" aria-label="Compass icon"></div><p class="lorem">Lorem Ipsum is simply dummy text of the printing and typesetting industry. Lorem Ipsum has been the industry's standard dummy text ever since the 1500s, when an unknown printer took a galley.</p><div class="more on">READ MORE</div></article>
  <article class="card" style="left:426px"><h3>PUBLIC RELATION<br>SERVICES</h3><div class="badge" role="img" aria-label="Cogs icon"></div><p class="lorem">Lorem Ipsum is simply dummy text of the printing and typesetting industry. Lorem Ipsum has been the industry's standard dummy text ever since the 1500s, when an unknown printer took a galley.</p><div class="more">READ MORE</div></article>
  <article class="card" style="left:640px"><h3>THOUGHT LEADER<br>DEVELOPMENT</h3><div class="badge" role="img" aria-label="Light bulb icon"></div><p class="lorem">Lorem Ipsum is simply dummy text of the printing and typesetting industry. Lorem Ipsum has been the industry's standard dummy text ever since the 1500s, when an unknown printer took a galley.</p><div class="more">READ MORE</div></article>
  <article class="card" style="left:854px"><h3 style="top:18px">TRAINING</h3><div class="badge" role="img" aria-label="Key icon"></div><p class="lorem">Lorem Ipsum is simply dummy text of the printing and typesetting industry. Lorem Ipsum has been the industry's standard dummy text ever since the 1500s, when an unknown printer took a galley.</p><div class="more">READ MORE</div></article>
</section>

<section class="abs mid">
  <h2 class="head" style="left:7px;top:24px">Welcome guest !</h2>
  <p class="lorem abs" style="left:7px;top:56px;width:406px">It is a long established fact that a reader will be distracted by the readable content of a page when looking at its layout. The point of using Lorem Ipsum is that it has a more-or-less normal distribution of letters, as opposed to using 'Content here, content here', making it look like readable English. It has survived not only five centuries, but also the leap into electronic typesetting, remaining essentially unchanged. Various versions have evolved over the years, sometimes by accident, sometimes on purpose (injected humour and</p>
  <div class="btn" style="left:7px;top:207px">Read More &gt;&gt;</div>
  <div class="abs" style="left:7px;top:280px;width:406px;height:1px;background:var(--line)"></div>
  <h2 class="head" style="left:7px;top:318px">Testimonials</h2>
  <p class="lorem quote abs" style="left:7px;top:352px;width:406px">Contrary to popular belief, Lorem Ipsum is not simply random text. It has roots in a piece of classical Latin literature from 45 BC, making it over 2000 years old. Paul Everly, a Latin professor at Harwick College .</p>
  <p class="abs quote" style="left:5px;top:430px;font-size:12px;line-height:17px;color:#555;font-weight:500">OWEN DARROW<br>IT MANAGER</p>
  <svg class="abs" style="left:374px;top:506px" width="40" height="18" viewBox="0 0 40 18"><path d="M9 3 3 9l6 6" fill="none" stroke="#333" stroke-width="2.5"/><path d="M28 3l6 6-6 6" fill="none" stroke="var(--orange)" stroke-width="2.5"/></svg>

  <div class="divider"></div>
  <h2 class="head" style="left:475px;top:24px">Company news &amp; events</h2>
  <div class="news-item" style="top:60px"><div class="news-img" role="img" aria-label="Photo of colleagues reviewing work at a laptop" style="background:linear-gradient(135deg,#cfd6df,#6b7480 60%,#2f3238)"></div><span class="news-date">11-07-2012</span><p class="lorem">Lorem Ipsum is simply dummy text of the printing and typesetting industry. Lorem Ipsum has been the industry's standard dummy text ever since the 1500s, when ...</p></div>
  <div class="abs" style="left:469px;top:198px;width:576px;height:1px;background:var(--line)"></div>
  <div class="news-item" style="top:213px"><div class="news-img" role="img" aria-label="Photo of a red arrow curving over a road" style="background:linear-gradient(160deg,#e9ecef,#b9bec4 55%,#c43a2c 56%,#7a7f86)"></div><span class="news-date">15-09-2012</span><p class="lorem">Lorem Ipsum is simply dummy text of the printing and typesetting industry. Lorem Ipsum has been the industry's standard dummy text ever since the 1500s, when ...</p></div>
  <div class="abs" style="left:469px;top:345px;width:576px;height:1px;background:var(--line)"></div>
  <div class="news-item" style="top:360px"><div class="news-img" role="img" aria-label="Photo of a globe resting on a keyboard" style="background:linear-gradient(135deg,#d7dde3,#5f8fc2 50%,#2d4f7a)"></div><span class="news-date">11-07-2012</span><p class="lorem">Lorem Ipsum is simply dummy text of the printing and typesetting industry. Lorem Ipsum has been the industry's standard dummy text ever since the 1500s, when ...</p></div>
  <div class="btn" style="left:469px;top:500px">Read More &gt;&gt;</div>
</section>

<section class="abs folks">
  <h2 class="head" style="left:7px;top:26px">Folks who dig us</h2>
  <div class="partners">
    <span class="partner"><i></i>Northline</span>
    <span class="partner">Ardent Coding</span>
    <span class="partner"><i style="border-radius:50%"></i>Keystep Systems</span>
    <span class="partner">Ridge Council</span>
    <span class="partner">Cedar Breath Clinic</span>
    <span class="partner">renewa</span>
  </div>
</section>

<footer class="abs footer">
  <h4 style="left:21px">ABOUT US</h4>
  <div class="abs" style="left:21px;top:60px;width:270px">
    <p style="font-size:10.5px;line-height:14px">Lorem Ipsum is simply dummy text of the printing and typesetting industry.</p>
    <p style="font-size:10.5px;line-height:14px;margin-top:10px">Lorem Ipsum has been the industry's standard dummy text ever since the 1500s, when an unknown printer took a galley of type and scrambled it to make a type specimen book. It has survived not only five centuries, but also the leap into electronic typesetting, remaining essentially unchanged.</p>
    <p style="margin-top:18px">&gt;&gt; <span class="hot">Read More</span></p>
  </div>
  <h4 style="left:348px">LINKS</h4>
  <ul class="abs" style="left:348px;top:54px;width:170px">
    <li>What's the Vantage?</li><li class="hot">Why the Vantage?</li><li>What's Up?</li><li>Who's Running Things</li><li>The Proof</li><li>Contact Us</li>
  </ul>
  <h4 style="left:534px">GET IN TOUCH</h4>
  <p class="abs" style="left:534px;top:54px;width:210px">B/118, Linden Avenue,<br>Harbor Road,<br>Millbrook, NC 07T.<br>Freephone :- +1800-555-0143<br><span style="padding-left:74px">+1800-555-0167</span><br>Facsimile :- +1800-555-0198<br>E-mail :- hello@vantage-mail.test</p>
  <h4 style="left:760px">HOW TO REACH US</h4>
  <div class="map" role="img" aria-label="Street map showing the office location"></div>
</footer>
<div class="abs copy">© COPYRIGHTS 2013. THE VANTAGE COMMUNICATION. ALL RIGHTS RESERVED.</div>

</body>
</html>
```